Cards and Stationary for natural and holistic Earthing/Grounding products
Solvana Portugal
Cards and Stationary for natural and holistic Earthing/Grounding products - Health
Creative Brief
Bright & Fun-filled
Miro T. Kastelan, PhD
Solvana Portugal Founder
Rua dos Pinheiros Altos 14 2615-117, Barcarena, Portugal
info@solvanaportugal.pt
www.solvanaportugal.pt
The back of the card should incorporate the logo and web address.

```html
<!DOCTYPE html>
<html lang="en">
<head>
<meta charset="utf-8">
<title>Solvana Portugal – Business Card</title>
<link href="https://fonts.googleapis.com/css2?family=Open+Sans:wght@400;600;700&display=swap" rel="stylesheet">
<style>
  :root {
    --bg: #e4e4e4;
    --card: #fbfbfb;
    --ink: #2b2b2b;
    --muted: #555555;
    --green: #4e9a2c;
    --rule: #d4d4d4;
  }
  * { margin: 0; padding: 0; box-sizing: border-box; }
  html, body {
    width: 1200px; height: 799px; overflow: hidden;
    background: var(--bg);
    font-family: "Open Sans", Arial, sans-serif;
  }
  .stage {
    position: relative; width: 1200px; height: 799px;
    display: flex; align-items: center; justify-content: center; gap: 60px;
  }
  .card {
    position: relative; width: 525px; height: 300px;
    background: var(--card);
    box-shadow: 0 6px 18px rgba(0,0,0,0.12);
  }
  /* Front */
  .holder { position: absolute; left: 34px; top: 36px; }
  .holder-name { font-size: 17px; font-weight: 700; color: var(--ink); }
  .holder-role { font-size: 13px; font-weight: 600; color: var(--green); margin-top: 3px; }
  .brand {
    display: flex; align-items: center; gap: 9px;
  }
  .brand-dot { width: 18px; height: 18px; border-radius: 50%; background: var(--green); }
  .brand-name { font-size: 22px; font-weight: 600; color: var(--green); }
  .card-front .brand { position: absolute; right: 30px; top: 58px; }
  .contacts { position: absolute; left: 34px; top: 150px; list-style: none; }
  .contacts li {
    display: flex; align-items: flex-start; gap: 10px;
    font-size: 11.5px; color: var(--muted); line-height: 1.4; margin-bottom: 9px;
  }
  .contacts svg { width: 12px; height: 12px; flex: none; margin-top: 2px; fill: var(--green); }
  .web-rule {
    position: absolute; left: 0; right: 0; bottom: 30px;
    border-top: 1px solid var(--rule);
  }
  .card-front .web {
    position: absolute; right: 30px; bottom: 12px;
    font-size: 11px; color: var(--green); font-weight: 600;
  }
  /* Back */
  .card-back {
    display: flex; flex-direction: column; align-items: center; justify-content: center; gap: 22px;
  }
  .card-back .brand-name { font-size: 30px; }
  .card-back .brand-dot { width: 24px; height: 24px; }
  .card-back .web { font-size: 12.5px; color: var(--green); font-weight: 600; }
</style>
</head>
<body>
<main class="stage">
  <section class="card card-front">
    <div class="holder">
      <h1 class="holder-name">Miro T. Kastelan, PhD</h1>
      <p class="holder-role">Solvana Portugal Founder</p>
    </div>
    <div class="brand">
      <span class="brand-dot"></span>
      <span class="brand-name">Solvana Portugal</span>
    </div>
    <ul class="contacts">
      <li>
        <svg viewBox="0 0 12 12"><path d="M6 0a4 4 0 0 0-4 4c0 3 4 8 4 8s4-5 4-8a4 4 0 0 0-4-4zm0 5.6A1.6 1.6 0 1 1 6 2.4a1.6 1.6 0 0 1 0 3.2z"/></svg>
        <span>Rua dos Pinheiros Altos 14<br>2615-117, Barcarena, Portugal</span>
      </li>
      <li>
        <svg viewBox="0 0 12 12"><path d="M2.4 0.6l2 2-1 1.4a7 7 0 0 0 4.6 4.6l1.4-1 2 2-1.2 1.8C5 11 1 7 0.6 1.8z"/></svg>
        <span>+351 912 408 375</span>
      </li>
      <li>
        <svg viewBox="0 0 12 12"><path d="M0 2h12v8H0zM1 3l5 3.6L11 3v-.2H1z"/></svg>
        <span>info@solvanaportugal.pt</span>
      </li>
    </ul>
    <div class="web-rule"></div>
    <p class="web">www.solvanaportugal.pt</p>
  </section>

  <section class="card card-back">
    <div class="brand">
      <span class="brand-dot"></span>
      <span class="brand-name">Solvana Portugal</span>
    </div>
    <p class="web">www.solvanaportugal.pt</p>
  </section>
</main>
</body>
</html>
```